Dust N Gone! Cleaning needs a flyer!

We have started a cleaning business DUST N GONE! Cleaning, and had a new logo design for it.
We would like a flyer designed to present to businesses that represents our professionalism, quality of service, security and value for money.
We would like a flyer that we can present to both our residential clients and business owners alike.
We will use this flyer for the next 2 years without having to make changes.
I'm happy for the designer to come up with their own wording if necessary.
Updates

Hello everyone!

In addition to the information I have already provided, please see below for more information to be included on the design for our flyer.

Thank you in advance.

Don’t read this unless your current cleaners are AMAZING!

Are you still reading? Now for the good news! Announcing the arrival of the amazing cleaning team of Dust N Gone! Cleaning. They’re the BEST in the Wimmera and we personally guarantee it.

We offer an ultimate service that NO other cleaning company in the Wimmera can offer; high quality cleaning of your home or business, carpet dry cleaning and pest control. All of these services can be completed at a time that is most convenient to you.

From wiping benches to washing windows, from dusting skirting boards to dry cleaning your carpets, from bathrooms to bugs, we really are your ONE stop shop.

Why choose the greatest cleaning company in the Wimmera?

For over 18 years, we have built a reputation on honesty and trust in the residential and commercial services. Our business is to know what people expect when we walk in to your home or business.

With our vast experience and knowledge, we know how to find the best people for the job, how to identify the best products for the clean, we use the newest of technology and equipment and have the best attitudes in town.

Local people, local business that you can rely on because we are also Dust N Gone! Pest Control & Fibrela all rolled in to your ONE stop shop for residential services.

Call us to discuss how we can give you the quality you demand.

Residential Cleaning                                                       Commercial Cleaning                                     

General house cleaning                                                  Business Premises          

Home help                                                                         Vacated properties

Rental vacancies                                                               Schools

Post renovation cleans                                                     Motels/Hotels

 

                                   

Target Market(s)

Business owners, commercial properties, home owners (women aged between 30 - 80y/o)

Industry/Entity Type

Residential

Requirements
Must have
• Incorporate our logo and colours.
Double sided.
Images of interiors of both home & office.
Catch phrase: "You demand quality ..... we guarantee it!"
Address: 22-26 Wattlegum St, Horsham VIC 3400
Phone: 1300 482 316
ABN: 47 308 562 194
We complete the ususal cleaning such as:
General House cleaning
Commercial Cleaning
Rental Properties
Business Premises
Other services we offer is:
Carpet dry cleaning
Upholstery cleaning
Dust N Gone! Mite Chasers pest control
Window cleaning.

```html
<!DOCTYPE html>
<html lang="en">
<head>
<meta charset="utf-8">
<title>Dust N Gone! Cleaning – Flyer</title>
<link rel="stylesheet" href="https://fonts.googleapis.com/css2?family=Open+Sans:wght@400;700&family=Roboto+Condensed:wght@700&display=swap">
<style>
  :root {
    --backdrop: #d9d9d9;
    --paper: #ffffff;
    --magenta: #ff14c8;
    --magenta-tint: #ffd9f5;
    --ink: #111111;
    --sky-top: #7fd3f5;
    --sky-bottom: #d8f2fc;
  }
  * { margin: 0; padding: 0; box-sizing: border-box; }
  html, body { width: 909px; height: 1200px; overflow: hidden; }
  body { background: var(--backdrop); font-family: "Open Sans", Arial, sans-serif; color: var(--ink); }

  .flyer {
    position: absolute; left: 93px; top: 84px;
    width: 724px; height: 1028px;
    background: var(--paper); overflow: hidden;
  }
  .sky-band { position: absolute; left: 0; top: 0; width: 724px; height: 290px; }

  .headline {
    position: absolute; left: 44px; top: 40px;
    font-family: "Roboto Condensed", "Arial Narrow", sans-serif;
    font-weight: 700; font-size: 66px; line-height: 66px;
    color: var(--magenta);
    transform: rotate(-4deg); transform-origin: left top;
  }

  .roof-graphic {
    position: absolute; left: 0; top: 600px; width: 724px; height: 320px;
    background: linear-gradient(180deg, var(--paper) 0%, var(--magenta-tint) 60%, var(--paper) 100%);
  }

  .product-photo {
    position: absolute; left: 465px; top: 300px; width: 255px; height: 490px;
    border-radius: 40px 40px 90px 90px;
    background: radial-gradient(ellipse at 45% 30%, #b9def2 0%, #dcecf4 45%, #f3e48a 75%, #ffffff 100%);
  }

  .services {
    position: absolute; left: 43px; top: 282px; width: 415px;
    font-size: 32px; line-height: 43px;
  }
  .services-title { font-weight: 700; }
  .services-list { list-style: none; }
  .services-list li { padding-left: 18px; text-indent: -18px; }
  .services-list li::before { content: "• "; }

  .brand {
    position: absolute; left: 92px; top: 818px;
    font-weight: 700; font-size: 42px; line-height: 48px; color: var(--ink);
  }

  .contact { position: absolute; top: 932px; font-size: 23px; line-height: 34px; }
  .contact-address { left: 92px; }
  .contact-phone { left: 429px; }
  .label { color: var(--magenta); font-weight: 700; }
</style>
</head>
<body>
  <main class="flyer">
    <svg class="sky-band" viewBox="0 0 724 290" role="img" aria-label="Blue band with soap bubbles">
      <defs>
        <linearGradient id="sky" x1="0" y1="0" x2="0" y2="1">
          <stop offset="0" stop-color="#d8f2fc"/>
          <stop offset="0.55" stop-color="#7fd3f5"/>
          <stop offset="1" stop-color="#4fbfee"/>
        </linearGradient>
      </defs>
      <path d="M0 0 H724 V210 C640 225 560 250 470 255 C360 262 300 230 200 235 C110 240 50 270 0 282 Z" fill="url(#sky)"/>
    </svg>

    <h1 class="headline">You demand quality...<br>we guarantee it!</h1>

    <div class="roof-graphic" role="img" aria-label="Magenta house roof outline graphic"></div>

    <div class="product-photo" role="img" aria-label="Bucket of cleaning sprays, cloths and yellow rubber gloves"></div>

    <section class="services">
      <p class="services-title">Other services<br>we offer is:</p>
      <ul class="services-list">
        <li>Carpet dry cleaning</li>
        <li>Upholstery cleaning</li>
        <li>Dust N Gone! Mite Chasers<br>pest control</li>
        <li>Window cleaning</li>
      </ul>
    </section>

    <p class="brand">DUST N GONE!<br>CLEANING</p>

    <p class="contact contact-address"><span class="label">Address:</span> 22-26 Wattlegum St,<br>Horsham VIC 3400</p>
    <p class="contact contact-phone"><span class="label">Phone:</span> 1300 482 316<br><span class="label">ABN:</span> 47 308 562 194</p>
  </main>
</body>
</html>
```